"MEET THE TEAM" page web design

We need a "meet the team" page for our website!
Please look at our website to see the style we need

We are looking for something unique, fun, cool, technology-style and yet professional. We plan on taking a picture of each employee (not sure if this will be a real photo/caricature/ black and white/goofy picture--> but we are open to any ideas you have that will work with the design) and putting it there, along with a little bio about each person.

Thanks! looking forward to working together:)
Updates

Project Deadline Extended
Reason: I am excited to see more designs and find the perfect fit. Thanks designers :)

Target Market(s)

People looking to purchase servers, workstations, components

Industry/Entity Type

Information Technology

Number of Pages Required

1 page

Font styles to use
Sans Serif
Other font styles liked:
• The font we use on our site so it matches

Requirements
Must have
• please look at our website qondimex.com and see the theme and colors we want.
• We have 13 employees but would like to have a design where we can add/remove people if we hire/terminate them without messing up the design.
• We are looking for something unique, fun, cool, technology-style and yet professional. We plan on taking a picture of each employee (not sure if this will be a real photo/caricature/ black and white/goofy picture--> but we are open to any ideas you have that will work with the design) and putting it there, along with a little bio about each person.
• We can upload anything you need
Nice to have
• We are also interested in having a design where when the cursor moves over a person then the bio comes out or moves around, or something. (This is not required, but we would love some cool ideas) And if you can come up with some design, we would have our programmers create it for us.
Should not have
• we are open to anything

```html
<!DOCTYPE html>
<html lang="en">
<head>
<meta charset="utf-8">
<title>Meet The Team – Qondimex</title>
<link href="https://fonts.googleapis.com/css2?family=Open+Sans:wght@300;400;600;700&display=swap" rel="stylesheet">
<style>
:root{
  --teal:#2aa79b;
  --ink:#3d4146;
  --muted:#8b9095;
  --line:#e2e4e6;
  --nav:#eef0f1;
  --page:#ffffff;
  --footer:#676b70;
  --footer-dark:#4c4f53;
  --footer-text:#e8eaec;
}
*{box-sizing:border-box;margin:0;padding:0}
html,body{width:816px;height:1200px;overflow:hidden}
body{font-family:"Open Sans",Arial,sans-serif;color:var(--ink);background:var(--page);position:relative}

/* header */
.site-header{height:74px;position:relative}
.brand-name{position:absolute;left:40px;top:20px;font-size:22px;font-weight:400;color:var(--ink);letter-spacing:.5px}
.header-tools{position:absolute;right:40px;top:26px;display:flex;align-items:center;gap:14px;font-size:11px;color:var(--muted)}
.tool{display:flex;align-items:center;gap:6px;white-space:nowrap}
.tool-circle{width:22px;height:22px;border:1px solid var(--line);border-radius:50%;display:flex;align-items:center;justify-content:center}
.phone-number{font-size:15px;font-weight:600;color:var(--ink)}

.main-nav{height:28px;background:var(--nav);border-top:1px solid var(--line);border-bottom:1px solid var(--line);display:flex;align-items:center;padding:0 40px;gap:15px;font-size:8.5px;font-weight:600;color:var(--ink);letter-spacing:.3px;white-space:nowrap}
.search{margin-left:auto;display:flex;align-items:center;gap:5px}
.search-box{width:90px;height:18px;background:#fff;border:1px solid var(--line);border-radius:2px;font-size:8px;color:var(--muted);padding:2px 6px;font-weight:400}
.search-btn{width:18px;height:18px;border-radius:50%;background:var(--teal)}

/* hero */
.hero{height:200px;position:relative;background:linear-gradient(180deg,#6f7b84 0%,#2e3840 45%,#1a2228 70%,#4a5660 100%);display:flex;align-items:flex-start;justify-content:center}
.hero h1{margin-top:48px;font-size:28px;font-weight:300;color:#fff}

.intro{position:relative;height:116px}
.intro-mark{position:absolute;left:40px;top:-14px;width:46px;height:56px;background:var(--teal)}
.intro p{position:absolute;left:104px;right:60px;top:22px;font-size:15px;line-height:23px;color:var(--ink)}

/* team grid */
.team-grid{position:absolute;left:40px;top:430px;width:736px;display:grid;grid-template-columns:repeat(3,1fr);gap:12px 14px}
.member-card{height:112px;border:1px solid var(--line);display:flex;background:#fff}
.member-card.is-active .member-info{background:#f1f2f3}
.member-photo{width:96px;height:100%;flex:none}
.photo-color{background:linear-gradient(160deg,#e9e3dc 0%,#c9b39f 55%,#7d6a5c 100%)}
.photo-mono{background:linear-gradient(160deg,#e2e2e2 0%,#9c9c9c 55%,#4e4e4e 100%)}
.member-info{flex:1;padding:10px 10px 0 12px;position:relative}
.member-name{font-size:11.5px;font-weight:400;color:var(--ink);white-space:nowrap}
.member-role{font-size:6.5px;font-weight:700;color:var(--teal);letter-spacing:.4px;margin-top:1px}
.member-rule{width:38px;height:2px;background:var(--teal);margin:10px 0 10px}
.member-links{display:flex;gap:8px;align-items:center}
.member-links .dot{width:7px;height:7px;border-radius:50%;background:var(--muted)}
.view-profile{position:absolute;left:12px;bottom:12px;font-size:6.5px;font-weight:700;color:var(--ink);letter-spacing:.3px}

/* footer */
.site-footer{position:absolute;left:0;top:815px;width:816px;height:385px;background:var(--footer);color:var(--footer-text)}
.footer-about{padding:24px 70px 0;text-align:center;font-size:9px;line-height:14px}
.footer-contact{display:flex;justify-content:space-between;padding:24px 110px 0 90px;font-size:9px}
.contact-item{display:flex;gap:8px;align-items:flex-start;line-height:13px}
.footer-links{display:flex;justify-content:space-between;margin:22px 40px 0;padding-top:14px;border-top:1px solid #7d8186;font-size:12px}
.footer-col{display:flex;flex-direction:column;gap:2px}
.footer-col small{font-size:7px;color:#c9cccf}
.socials{display:flex;justify-content:center;gap:12px;margin-top:34px}
.socials span{width:22px;height:22px;border:1px solid #9a9ea3;border-radius:50%}
.footer-bottom{position:absolute;left:0;bottom:0;width:100%;height:44px;background:var(--footer-dark);text-align:center;font-size:7px;line-height:11px;padding-top:11px;color:#cfd2d5}
</style>
</head>
<body>

<header class="site-header">
  <span class="brand-name">Qondimex</span>
  <div class="header-tools">
    <div class="tool"><span class="tool-circle">
      <svg width="11" height="11" viewBox="0 0 12 12"><path d="M1 2h2l1.5 6h5.5l1-4H4" fill="none" stroke="#8b9095" stroke-width="1.2"/><circle cx="5" cy="10.5" r="1" fill="#8b9095"/><circle cx="9" cy="10.5" r="1" fill="#8b9095"/></svg>
    </span>VIEW CART</div>
    <div class="tool"><span class="tool-circle">
      <svg width="11" height="11" viewBox="0 0 12 12"><path d="M3 1l2 2.5-1.2 1.3a6 6 0 0 0 3.4 3.4L8.5 7 11 9l-1.3 2A9 9 0 0 1 1 2.3z" fill="#8b9095"/></svg>
    </span><span class="phone-number">555-014-2290</span></div>
  </div>
</header>

<nav class="main-nav">
  <span>SERVERS</span><span>WORKSTATIONS</span><span>COMPONENTS</span><span>VIRTUAL REALITY</span><span>DRONES</span><span>ABOUT US</span><span>BLOG</span><span>FREEBIES</span><span>CONTACT US</span>
  <div class="search"><span class="search-box">Search</span><span class="search-btn"></span></div>
</nav>

<section class="hero" role="img" aria-label="Photo of a modern glass office building seen from below">
  <h1>Meet The Team</h1>
</section>

<section class="intro">
  <span class="intro-mark"></span>
  <p>Morbi non mauris nec ipsum bibendum luctus. Mauris sollicitudin purus quis arcu fringilla pretium. Aliquam vestibulum quis lorem vulputate.</p>
</section>

<main class="team-grid">
  <article class="member-card"><div class="member-photo photo-color" role="img" aria-label="Portrait of Julia Marlow"></div><div class="member-info"><h2 class="member-name">Julia Marlow</h2><p class="member-role">SENIOR EXECUTIVE</p><div class="member-rule"></div><div class="member-links"><svg width="8" height="8" viewBox="0 0 12 12"><path d="M3 1l2 2.5-1.2 1.3a6 6 0 0 0 3.4 3.4L8.5 7 11 9l-1.3 2A9 9 0 0 1 1 2.3z" fill="#8b9095"/></svg><svg width="9" height="7" viewBox="0 0 12 9"><rect x=".5" y=".5" width="11" height="8" fill="none" stroke="#8b9095"/><path d="M.5.5 6 5l5.5-4.5" fill="none" stroke="#8b9095"/></svg><span class="dot"></span><span class="dot"></span></div><span class="view-profile">VIEW PROFILE ›</span></div></article>

  <article class="member-card is-active"><div class="member-photo photo-mono" role="img" aria-label="Black and white portrait of Mark Ellison"></div><div class="member-info"><h2 class="member-name">Mark Ellison</h2><p class="member-role">SENIOR EXECUTIVE</p><div class="member-rule"></div><div class="member-links"><svg width="8" height="8" viewBox="0 0 12 12"><path d="M3 1l2 2.5-1.2 1.3a6 6 0 0 0 3.4 3.4L8.5 7 11 9l-1.3 2A9 9 0 0 1 1 2.3z" fill="#8b9095"/></svg><svg width="9" height="7" viewBox="0 0 12 9"><rect x=".5" y=".5" width="11" height="8" fill="none" stroke="#8b9095"/><path d="M.5.5 6 5l5.5-4.5" fill="none" stroke="#8b9095"/></svg><span class="dot"></span><span class="dot"></span></div><span class="view-profile">VIEW PROFILE ›</span></div></article>

  <article class="member-card"><div class="member-photo photo-color" role="img" aria-label="Portrait of Melissa Brandt"></div><div class="member-info"><h2 class="member-name">Melissa Brandt</h2><p class="member-role">SENIOR EXECUTIVE</p><div class="member-rule"></div><div class="member-links"><svg width="8" height="8" viewBox="0 0 12 12"><path d="M3 1l2 2.5-1.2 1.3a6 6 0 0 0 3.4 3.4L8.5 7 11 9l-1.3 2A9 9 0 0 1 1 2.3z" fill="#8b9095"/></svg><svg width="9" height="7" viewBox="0 0 12 9"><rect x=".5" y=".5" width="11" height="8" fill="none" stroke="#8b9095"/><path d="M.5.5 6 5l5.5-4.5" fill="none" stroke="#8b9095"/></svg><span class="dot"></span><span class="dot"></span></div><span class="view-profile">VIEW PROFILE ›</span></div></article>

  <article class="member-card"><div class="member-photo photo-color" role="img" aria-label="Portrait of Melissa Brandt"></div><div class="member-info"><h2 class="member-name">Melissa Brandt</h2><p class="member-role">SENIOR EXECUTIVE</p><div class="member-rule"></div><div class="member-links"><svg width="8" height="8" viewBox="0 0 12 12"><path d="M3 1l2 2.5-1.2 1.3a6 6 0 0 0 3.4 3.4L8.5 7 11 9l-1.3 2A9 9 0 0 1 1 2.3z" fill="#8b9095"/></svg><svg width="9" height="7" viewBox="0 0 12 9"><rect x=".5" y=".5" width="11" height="8" fill="none" stroke="#8b9095"/><path d="M.5.5 6 5l5.5-4.5" fill="none" stroke="#8b9095"/></svg><span class="dot"></span><span class="dot"></span></div><span class="view-profile">VIEW PROFILE ›</span></div></article>

  <article class="member-card"><div class="member-photo photo-color" role="img" aria-label="Portrait of Julia Marlow"></div><div class="member-info"><h2 class="member-name">Julia Marlow</h2><p class="member-role">SENIOR EXECUTIVE</p><div class="member-rule"></div><div class="member-links"><svg width="8" height="8" viewBox="0 0 12 12"><path d="M3 1l2 2.5-1.2 1.3a6 6 0 0 0 3.4 3.4L8.5 7 11 9l-1.3 2A9 9 0 0 1 1 2.3z" fill="#8b9095"/></svg><svg width="9" height="7" viewBox="0 0 12 9"><rect x=".5" y=".5" width="11" height="8" fill="none" stroke="#8b9095"/><path d="M.5.5 6 5l5.5-4.5" fill="none" stroke="#8b9095"/></svg><span class="dot"></span><span class="dot"></span></div><span class="view-profile">VIEW PROFILE ›</span></div></article>

  <article class="member-card"><div class="member-photo photo-color" role="img" aria-label="Portrait of Mark Ellison"></div><div class="member-info"><h2 class="member-name">Mark Ellison</h2><p class="member-role">SENIOR EXECUTIVE</p><div class="member-rule"></div><div class="member-links"><svg width="8" height="8" viewBox="0 0 12 12"><path d="M3 1l2 2.5-1.2 1.3a6 6 0 0 0 3.4 3.4L8.5 7 11 9l-1.3 2A9 9 0 0 1 1 2.3z" fill="#8b9095"/></svg><svg width="9" height="7" viewBox="0 0 12 9"><rect x=".5" y=".5" width="11" height="8" fill="none" stroke="#8b9095"/><path d="M.5.5 6 5l5.5-4.5" fill="none" stroke="#8b9095"/></svg><span class="dot"></span><span class="dot"></span></div><span class="view-profile">VIEW PROFILE ›</span></div></article>

  <article class="member-card"><div class="member-photo photo-color" role="img" aria-label="Portrait of Julia Marlow"></div><div class="member-info"><h2 class="member-name">Julia Marlow</h2><p class="member-role">SENIOR EXECUTIVE</p><div class="member-rule"></div><div class="member-links"><svg width="8" height="8" viewBox="0 0 12 12"><path d="M3 1l2 2.5-1.2 1.3a6 6 0 0 0 3.4 3.4L8.5 7 11 9l-1.3 2A9 9 0 0 1 1 2.3z" fill="#8b9095"/></svg><svg width="9" height="7" viewBox="0 0 12 9"><rect x=".5" y=".5" width="11" height="8" fill="none" stroke="#8b9095"/><path d="M.5.5 6 5l5.5-4.5" fill="none" stroke="#8b9095"/></svg><span class="dot"></span><span class="dot"></span></div><span class="view-profile">VIEW PROFILE ›</span></div></article>

  <article class="member-card"><div class="member-photo photo-color" role="img" aria-label="Portrait of Mark Ellison"></div><div class="member-info"><h2 class="member-name">Mark Ellison</h2><p class="member-role">SENIOR EXECUTIVE</p><div class="member-rule"></div><div class="member-links"><svg width="8" height="8" viewBox="0 0 12 12"><path d="M3 1l2 2.5-1.2 1.3a6 6 0 0 0 3.4 3.4L8.5 7 11 9l-1.3 2A9 9 0 0 1 1 2.3z" fill="#8b9095"/></svg><svg width="9" height="7" viewBox="0 0 12 9"><rect x=".5" y=".5" width="11" height="8" fill="none" stroke="#8b9095"/><path d="M.5.5 6 5l5.5-4.5" fill="none" stroke="#8b9095"/></svg><span class="dot"></span><span class="dot"></span></div><span class="view-profile">VIEW PROFILE ›</span></div></article>

  <article class="member-card"><div class="member-photo photo-color" role="img" aria-label="Portrait of Melissa Brandt"></div><div class="member-info"><h2 class="member-name">Melissa Brandt</h2><p class="member-role">SENIOR EXECUTIVE</p><div class="member-rule"></div><div class="member-links"><svg width="8" height="8" viewBox="0 0 12 12"><path d="M3 1l2 2.5-1.2 1.3a6 6 0 0 0 3.4 3.4L8.5 7 11 9l-1.3 2A9 9 0 0 1 1 2.3z" fill="#8b9095"/></svg><svg width="9" height="7" viewBox="0 0 12 9"><rect x=".5" y=".5" width="11" height="8" fill="none" stroke="#8b9095"/><path d="M.5.5 6 5l5.5-4.5" fill="none" stroke="#8b9095"/></svg><span class="dot"></span><span class="dot"></span></div><span class="view-profile">VIEW PROFILE ›</span></div></article>
</main>

<footer class="site-footer">
  <p class="footer-about">Based in Fairlake, California, Qondimex offers custom servers, storage, and workstations for local businesses in the surrounding valley, coastal cities and nearby counties. Qondimex also offers its products to clients throughout the United States and worldwide.</p>
  <div class="footer-contact">
    <div class="contact-item"><svg width="10" height="13" viewBox="0 0 10 13"><path d="M5 12S1 7.5 1 4.8a4 4 0 0 1 8 0C9 7.5 5 12 5 12z" fill="none" stroke="#e8eaec"/><circle cx="5" cy="4.8" r="1.4" fill="#e8eaec"/></svg><span>2200 Orrin Way<br>Fairlake, CA 90000</span></div>
    <div class="contact-item"><svg width="11" height="11" viewBox="0 0 12 12"><path d="M3 1l2 2.5-1.2 1.3a6 6 0 0 0 3.4 3.4L8.5 7 11 9l-1.3 2A9 9 0 0 1 1 2.3z" fill="#e8eaec"/></svg><span>555-014-2290</span></div>
    <div class="contact-item"><svg width="12" height="9" viewBox="0 0 12 9"><rect x=".5" y=".5" width="11" height="8" fill="none" stroke="#e8eaec"/><path d="M.5.5 6 5l5.5-4.5" fill="none" stroke="#e8eaec"/></svg><span>sales@qondimex.com</span></div>
  </div>
  <div class="footer-links">
    <div class="footer-col">Computer Hardware</div>
    <div class="footer-col">Drones</div>
    <div class="footer-col">Virtual Reality</div>
    <div class="footer-col">About Us</div>
    <div class="footer-col">Customer Support<small>Returns &amp; Warranty</small><small>Shipping Policy</small><small>Contact Us</small></div>
  </div>
  <div class="socials"><span></span><span></span><span></span><span></span></div>
  <div class="footer-bottom">Qondimex LLC<br>Copyright © 2017</div>
</footer>

</body>
</html>
```